Bright Harbor Health (03)

We're designing a website to sell Medicare Supplements. Attached is the script we want to say and general layout, but please use your best knowledge to make it better. This platform should be extremely user-friendly, but we want to make it look fun and approachable! Most Insurance/medicare websites are very boring, drab, simple but we want this one to be more personalized, fun and sexy (but again, still user-friendly since our target demographic is 65+).

This homepage should include a fun and inviting quiz, the script is in the attachment below. It should also include the blurbs about what medicare supplements plans are and why they should buy them. Feel free to play around with cool fonts and imagery, we want the site to be engaging!

Target Market(s)

seniors

Industry/Entity Type

Insurance

Number of Pages Required

1 page

Requirements
Must have
• Quiz, company name and tag line, script
Nice to have
• fun, engaging elements

```html
<!DOCTYPE html>
<html lang="en">
<head>
<meta charset="utf-8">
<title>Bright Harbor Health — Medicare Supplement Plans</title>
<link href="https://fonts.googleapis.com/css2?family=Lato:ital,wght@0,400;0,700;1,400&family=Open+Sans:wght@600;700&display=swap" rel="stylesheet">
<style>
:root{
  --brand-blue:#1a7ab8;
  --brand-red:#c8161d;
  --brand-green:#8db535;
  --ink:#222;
  --text:#333;
  --muted-bg:#f3f3f3;
  --footer-bg:#2b2b2b;
  --line:#e2e2e2;
  --white:#fff;
}
*{box-sizing:border-box;margin:0;padding:0}
html,body{width:1200px;height:2292px;overflow:hidden}
body{font-family:"Lato",sans-serif;color:var(--text);background:var(--white);position:relative}
.site-header{position:absolute;top:0;left:0;width:1200px;height:90px;background:var(--white)}
.brand{position:absolute;left:78px;top:26px;display:flex;align-items:center;gap:10px;font-family:"Lato",sans-serif;font-weight:700;font-size:22px;color:var(--ink)}
.brand-dot{width:38px;height:38px;border-radius:50%;background:var(--brand-green)}
.main-nav{position:absolute;top:41px;left:0;font-weight:700;font-size:14px;color:var(--ink)}
.main-nav a{position:absolute;white-space:nowrap;text-decoration:none;color:inherit}
.main-nav a.is-active{color:var(--brand-blue)}
.quote-btn{position:absolute;left:932px;top:28px;width:194px;height:42px;background:var(--brand-red);color:var(--white);font-family:"Open Sans",sans-serif;font-weight:700;font-size:18px;display:flex;align-items:center;justify-content:center;border-radius:2px}
.hero{position:absolute;top:90px;left:0;width:1200px;height:651px;background:linear-gradient(100deg,#7d8088 0%,#a7a4a0 35%,#b59a7e 60%,#8e857a 100%)}
.hero::after{content:"";position:absolute;inset:0;background:rgba(30,30,35,.35)}
.hero-copy{position:absolute;top:0;left:0;width:1200px;text-align:center;color:var(--white);z-index:1}
.hero-title{position:absolute;top:150px;width:100%;font-family:"Open Sans",sans-serif;font-weight:700;font-size:59px;letter-spacing:.5px}
.hero-sub{position:absolute;top:230px;width:100%;font-family:"Open Sans",sans-serif;font-weight:600;font-size:35px;line-height:44px}
.hero-text{position:absolute;top:330px;left:150px;width:900px;font-size:17.5px;line-height:30px}
.hero-call{position:absolute;top:405px;width:100%;font-family:"Open Sans",sans-serif;font-weight:700;font-size:31px}
.quiz{position:absolute;top:594px;left:75px;width:1051px;height:332px;background:var(--white);border-radius:6px 6px 0 0;z-index:2}
.quiz-heading{position:absolute;top:31px;left:0;width:100%;text-align:center;font-family:"Open Sans",sans-serif;font-weight:600;font-size:24px;line-height:35px;color:var(--brand-blue)}
.quiz-group{position:absolute;top:130px}
.quiz-group h3{font-family:"Open Sans",sans-serif;font-weight:600;font-size:21px;color:var(--ink);margin-bottom:10px}
.quiz-option{display:flex;align-items:center;height:34.5px;font-size:17.5px;color:var(--ink)}
.quiz-option span.radio{width:15px;height:15px;border:1px solid #aaa;border-radius:50%;margin-right:18px;margin-left:-1px}
.zip-input{position:absolute;left:764px;top:151px;width:231px;height:39px;border:1px solid #999;display:flex;align-items:center;justify-content:center;font-size:15px;color:var(--ink)}
.quiz-submit{position:absolute;left:764px;top:201px;width:231px;height:39px;background:var(--brand-green)}
.about{position:absolute;top:926px;left:0;width:1200px;height:493px;background:var(--muted-bg)}
.about-photo{position:absolute;left:0;top:0;width:497px;height:493px;background:linear-gradient(120deg,#6f6a64 0%,#c9a36a 45%,#d8b23a 70%,#e0a65a 100%)}
.about-body{position:absolute;left:524px;top:58px;width:590px}
.about-body h2{font-family:"Open Sans",sans-serif;font-weight:700;font-size:32px;color:var(--ink);margin-bottom:18px}
.about-body p{font-size:14.5px;line-height:27.7px}
.ticks{list-style:none;margin-top:18px}
.ticks li{position:relative;padding-left:33px;font-size:14.5px;line-height:27.7px;margin-bottom:6.5px}
.ticks svg{position:absolute;left:0;top:7px}
.costs{position:absolute;top:1460px;left:75px;width:1051px;text-align:center}
.costs h2{font-family:"Open Sans",sans-serif;font-weight:700;font-size:32px;color:var(--ink)}
.costs p.lead{margin-top:16px;font-size:14.5px;line-height:27.7px}
.cost-card{position:absolute;top:1662px;width:329px;height:330px;border:1px solid var(--line);text-align:center;background:var(--white)}
.cost-icon{margin:31px auto 0;width:79px;height:79px;border:1px solid var(--line);border-radius:50%;display:flex;align-items:center;justify-content:center}
.cost-card h3{margin-top:20px;font-family:"Open Sans",sans-serif;font-weight:700;font-size:25px;line-height:30px;color:var(--brand-blue)}
.cost-card p{margin:14px 22px 0;font-size:14.5px;line-height:27.7px}
.costs-note{position:absolute;top:2022px;left:150px;width:900px;text-align:center;font-style:italic;font-size:17.5px;line-height:31px;color:var(--ink)}
.site-footer{position:absolute;top:2144px;left:0;width:1200px;height:148px;background:var(--footer-bg);text-align:center;color:#ccc}
.site-footer p{margin-top:40px;font-size:14.5px}
.social{display:flex;justify-content:center;gap:22px;margin-top:18px}
.social span{width:26px;height:26px;border-radius:50%;background:var(--white)}
</style>
</head>
<body>
<header class="site-header">
  <div class="brand"><span class="brand-dot"></span>Bright Harbor Health</div>
  <nav class="main-nav">
    <a class="is-active" style="left:398px">HOME</a>
    <a style="left:478px">ABOUT US</a>
    <a style="left:585px">BLOG</a>
    <a style="left:659px">MEDICARE PLANS</a>
    <a style="left:818px">CONTACT US</a>
  </nav>
  <a class="quote-btn">Get A Free Quote</a>
</header>

<section class="hero">
  <div role="img" aria-label="Smiling senior couple relaxing on a sofa at home" style="position:absolute;inset:0"></div>
  <div class="hero-copy">
    <h1 class="hero-title">BRIGHT HARBOR HEALTH</h1>
    <p class="hero-sub">Be confident in choosing the Medicare Supplement<br>plan that’s right for you.</p>
    <p class="hero-text">We know insurance can be confusing. With so much information and not enough answers, we’re here to help you find the plan that works best for you, your family and your health.</p>
    <p class="hero-call">Call (800) 555-0142 to Talk to a Live Agent.</p>
  </div>
</section>

<section class="quiz">
  <h2 class="quiz-heading">Take this short quiz to to find flexible and affordable plans that you<br>can feel confident in.</h2>
  <div class="quiz-group" style="left:58px">
    <h3>I am</h3>
    <div class="quiz-option"><span class="radio"></span>Over 64 years old</div>
    <div class="quiz-option"><span class="radio"></span>64 years old</div>
    <div class="quiz-option"><span class="radio"></span>Under 64 years old</div>
  </div>
  <div class="quiz-group" style="left:332px">
    <h3>I am</h3>
    <div class="quiz-option"><span class="radio"></span>Male</div>
    <div class="quiz-option"><span class="radio"></span>Female</div>
    <div class="quiz-option"><span class="radio"></span>Unspecified</div>
  </div>
  <div class="quiz-group" style="left:542px">
    <h3>I want to see</h3>
    <div class="quiz-option"><span class="radio"></span>Free plans</div>
    <div class="quiz-option"><span class="radio"></span>Premium plans</div>
    <div class="quiz-option"><span class="radio"></span>All plans</div>
  </div>
  <div class="zip-input">Enter Zip Code</div>
  <div class="quiz-submit"></div>
</section>

<section class="about">
  <div class="about-photo" role="img" aria-label="Senior couple reviewing plans together on a laptop"></div>
  <div class="about-body">
    <h2>What is a Medicare Supplement plan?</h2>
    <p>Each Medicare Supplement insurance plan offers a different level of basic benefits, but each lettered plan will include the same standardized basic benefits regardless of insurance company and location. Medicare Supplement insurance plans do not always cover vision, dental, long-term care, or hearing aids, but all plans must cover at least a portion of the following basic benefits:</p>
    <ul class="ticks">
      <li><svg width="14" height="14" viewBox="0 0 14 14"><circle cx="7" cy="7" r="7" fill="#1a7ab8"/><path d="M3.8 7.2l2.2 2.2 4.2-4.4" stroke="#fff" stroke-width="1.8" fill="none"/></svg>Medicare Part A coinsurance costs up to an additional 365 days after Medicare benefits are exhausted</li>
      <li><svg width="14" height="14" viewBox="0 0 14 14"><circle cx="7" cy="7" r="7" fill="#1a7ab8"/><path d="M3.8 7.2l2.2 2.2 4.2-4.4" stroke="#fff" stroke-width="1.8" fill="none"/></svg>Medicare Part A hospice care coinsurance or copayments</li>
      <li><svg width="14" height="14" viewBox="0 0 14 14"><circle cx="7" cy="7" r="7" fill="#1a7ab8"/><path d="M3.8 7.2l2.2 2.2 4.2-4.4" stroke="#fff" stroke-width="1.8" fill="none"/></svg>Medicare Part B coinsurance or copayments</li>
      <li><svg width="14" height="14" viewBox="0 0 14 14"><circle cx="7" cy="7" r="7" fill="#1a7ab8"/><path d="M3.8 7.2l2.2 2.2 4.2-4.4" stroke="#fff" stroke-width="1.8" fill="none"/></svg>First three pints of blood used in a medical procedure</li>
    </ul>
  </div>
</section>

<section class="costs">
  <h2>Medicare Supplement insurance plan costs</h2>
  <p class="lead">Although private insurance companies are required to offer the same basic benefits for each lettered plan, they do have the ability to charge different premiums. You might want to shop around to find a Medicare Supplement insurance plan that may fit your medical and financial needs. Insurance companies may price their plan premiums in any of the following ways:</p>
</section>

<article class="cost-card" style="left:75px">
  <div class="cost-icon"><svg width="46" height="40" viewBox="0 0 46 40" fill="none" stroke-width="1.6"><circle cx="12" cy="14" r="5" stroke="#c8161d"/><circle cx="34" cy="14" r="5" stroke="#c8161d"/><circle cx="23" cy="18" r="5" stroke="#8db535"/><path d="M4 34c0-6 4-10 8-10s8 4 8 10M26 34c0-6 4-10 8-10s8 4 8 10M14 38c0-6 4-10 9-10s9 4 9 10" stroke="#c8161d"/></svg></div>
  <h3>Community<br>No-Age-Rated</h3>
  <p>These Medicare Supplement insurance plans charge premiums that are the same across the board, regardless of age.</p>
</article>
<article class="cost-card" style="left:436px">
  <div class="cost-icon"><svg width="46" height="40" viewBox="0 0 46 40" fill="none" stroke-width="1.6"><rect x="5" y="4" width="32" height="32" stroke="#c8161d"/><path d="M5 11h32" stroke="#c8161d"/><path d="M10 18h18M10 24h14M10 30h10" stroke="#8db535"/><path d="M30 30l10-12 3 3-10 12-4 1z" stroke="#c8161d"/></svg></div>
  <h3>Issue-Age-Rated</h3>
  <p>These plans base their premiums on your age when you first enrolled in the policy. Therefore, the younger you are when you enroll in this type of plan, the lower your premium will be.</p>
</article>
<article class="cost-card" style="left:797px">
  <div class="cost-icon"><svg width="46" height="40" viewBox="0 0 46 40" fill="none" stroke-width="1.6"><rect x="6" y="3" width="26" height="34" stroke="#c8161d"/><circle cx="14" cy="11" r="4" stroke="#8db535"/><path d="M21 10h7M21 14h7M11 22h15M11 28h10" stroke="#c8161d"/><path d="M36 20l7 3v6c0 4-3 7-7 8-4-1-7-4-7-8v-6z" stroke="#c8161d"/><path d="M36 26v6M33 29h6" stroke="#8db535"/></svg></div>
  <h3>Attained-Age-Rated</h3>
  <p>Like issue-age-rated, these plans base their premiums on the age you were when you first bought a policy, but unlike issue-age-rated, premiums increase as you get older.</p>
</article>

<p class="costs-note">Please note that no matter what rating method an insurance company uses, premiums may increase over time for reasons other than age, such as inflation.</p>

<footer class="site-footer">
  <p>Copyright © 2020, Company Name All Right reserved</p>
  <div class="social">
    <span aria-label="Social link"></span><span aria-label="Social link"></span><span aria-label="Social link"></span><span aria-label="Social link"></span><span aria-label="Social link"></span>
  </div>
</footer>
</body>
</html>
```